Stationery Design Project

We need a Stationery Design for automotive industry.
Updates

Target Market(s)

Mechanic garage and Mechanics

Industry/Entity Type

Automotive

Requirements
Must have
• The logo company and the legal information.

We are a car spart parts and tools delar
Nice to have
• We like something elegant and simple.

```html
<!DOCTYPE html>
<html lang="en">
<head>
<meta charset="utf-8">
<title>Velora Motor Supply – Stationery</title>
<link href="https://fonts.googleapis.com/css2?family=Arimo:wght@400;700&display=swap" rel="stylesheet">
<style>
  :root {
    --backdrop: #d9d9d9;
    --paper: #ffffff;
    --ink: #3a3a3a;
    --ink-dark: #1a1a1a;
    --accent: #5a63b5;
    --card-black: #0d0d0d;
    --silver-light: #f4f4f4;
    --silver-mid: #c9c9c9;
    --silver-dark: #9a9a9a;
    --edge: #bdbdbd;
  }
  * { margin: 0; padding: 0; box-sizing: border-box; }
  html, body { width: 1200px; height: 849px; overflow: hidden; }
  body {
    position: relative;
    background: var(--backdrop);
    font-family: "Arimo", Arial, sans-serif;
    color: var(--ink);
  }
  .sheet {
    position: absolute;
    background: var(--paper);
    box-shadow: 0 1px 4px rgba(0,0,0,.25);
  }
  .silver-band {
    position: absolute;
    left: 0; right: 0;
    background: linear-gradient(90deg, var(--silver-dark) 0%, var(--silver-light) 18%, var(--silver-mid) 40%, var(--silver-light) 60%, var(--silver-mid) 82%, var(--silver-dark) 100%);
    display: flex;
    align-items: center;
    justify-content: center;
    gap: 8px;
  }
  .brand-name {
    font-weight: 700;
    color: var(--ink-dark);
    letter-spacing: .04em;
    white-space: nowrap;
  }
  .brand-dot {
    border-radius: 50%;
    background: var(--ink-dark);
  }
  .accent { color: var(--accent); font-weight: 700; }

  /* Letterhead */
  .letterhead { left: 28px; top: 40px; width: 594px; height: 770px; }
  .letterhead .silver-band { top: 30px; height: 40px; }
  .letterhead .brand-name { font-size: 20px; }
  .letterhead .brand-dot { width: 14px; height: 14px; }
  .letterhead-footer {
    position: absolute; left: 0; right: 0; bottom: 16px;
    text-align: center; font-size: 8px; line-height: 12px;
  }
  .letterhead-footer .legal-abn { margin-top: 10px; }

  /* Business card front */
  .card-front { left: 580px; top: 160px; width: 245px; height: 140px; }
  .card-front .silver-band { top: 20px; height: 28px; }
  .card-front .brand-name { font-size: 11px; }
  .card-front .brand-dot { width: 8px; height: 8px; }
  .card-person { position: absolute; top: 76px; left: 0; right: 0; text-align: center; }
  .person-name { font-size: 10px; font-weight: 700; color: var(--ink-dark); }
  .person-role { font-size: 8px; color: var(--accent); margin-top: 1px; }
  .card-contact {
    position: absolute; bottom: 8px; left: 0; right: 0;
    text-align: center; font-size: 5.6px; line-height: 8px;
  }

  /* Business card back */
  .card-back {
    left: 858px; top: 160px; width: 245px; height: 140px;
    background: var(--card-black);
    display: flex; align-items: center; justify-content: center; gap: 8px;
  }
  .card-back .brand-name { color: #ffffff; font-size: 14px; }

  /* Envelope */
  .envelope { left: 510px; top: 326px; width: 648px; height: 407px; background: transparent; box-shadow: none; }
  .envelope-shape { position: absolute; inset: 0; }
  .envelope-flap-text {
    position: absolute; left: 0; right: 0; top: 14px; height: 100px;
    transform: rotate(180deg);
    text-align: center; font-size: 6.5px; line-height: 10px;
    display: flex; flex-direction: column; justify-content: flex-start;
  }
  .envelope-flap-text .flap-brand {
    display: flex; justify-content: center; align-items: center; gap: 6px; margin-bottom: 6px;
  }
  .envelope-flap-text .brand-name { font-size: 11px; }
  .envelope-flap-text .brand-dot { width: 8px; height: 8px; }
  .envelope-flap-text .legal-abn { margin-top: 6px; }
  .envelope .silver-band { top: 342px; height: 36px; justify-content: flex-start; padding-left: 40px; }
  .envelope .brand-name { font-size: 17px; }
  .envelope .silver-band .brand-dot { width: 12px; height: 12px; }
</style>
</head>
<body>

  <section class="sheet letterhead" aria-label="Letterhead">
    <div class="silver-band">
      <span class="brand-dot"></span>
      <span class="brand-name">Velora Motor Supply</span>
    </div>
    <footer class="letterhead-footer">
      <div class="accent">Velora Motor Supply Pty Ltd.</div>
      <div>P.O. Box 000. Sydney NSW 0000 I <span class="accent">Phone</span> (02) 0000 0000 I <span class="accent">Fax</span> (02) 0000 0000 I info@veloramotor.com.au I www.veloramotor.com.au</div>
      <div class="legal-abn">ABN 48 302 117 564</div>
    </footer>
  </section>

  <section class="sheet card-front" aria-label="Business card front">
    <div class="silver-band">
      <span class="brand-dot"></span>
      <span class="brand-name">Velora Motor Supply</span>
    </div>
    <div class="card-person">
      <div class="person-name">Daniel Marsh</div>
      <div class="person-role">Director</div>
    </div>
    <div class="card-contact">
      <div>P.O. Box 000. Sydney NSW 0000 I <span class="accent">Phone</span> (02) 0000 0000 I <span class="accent">Fax</span> (02) 0000 0000</div>
      <div>info@veloramotor.com.au I www.veloramotor.com.au</div>
    </div>
  </section>

  <section class="sheet card-back" aria-label="Business card back">
    <span class="brand-dot" style="width:10px;height:10px;background:#fff"></span>
    <span class="brand-name">Velora Motor Supply</span>
  </section>

  <section class="sheet envelope" aria-label="Envelope">
    <svg class="envelope-shape" width="648" height="407" viewBox="0 0 648 407">
      <path d="M0 119 L0 22 Q0 2 22 2 L626 2 Q644 2 646 22 L648 119 L648 407 L0 407 Z"
            fill="#ffffff" stroke="#bdbdbd" stroke-width="1"/>
      <line x1="0" y1="119" x2="648" y2="119" stroke="#bdbdbd" stroke-width="1"/>
    </svg>
    <div class="envelope-flap-text">
      <div class="flap-brand">
        <span class="brand-dot"></span>
        <span class="brand-name">Velora Motor Supply</span>
      </div>
      <div class="accent">Velora Motor Supply Pty Ltd.</div>
      <div>P.O. Box 000. Sydney NSW 0000 I <span class="accent">Phone</span> (02) 0000 0000 I <span class="accent">Fax</span> (02) 0000 0000 I info@veloramotor.com.au I www.veloramotor.com.au</div>
      <div class="legal-abn">ABN 48 302 117 564</div>
    </div>
    <div class="silver-band">
      <span class="brand-dot"></span>
      <span class="brand-name">Velora Motor Supply</span>
    </div>
  </section>

</body>
</html>
```